Board Presentation template

Design a simple and clean PowerPoint slide templates for a Board meeting. The slides should have predominantly white backgrounds and use the colors of our Logo (attached): Tones of grey and orange and blue.
The company name is called Harbor Lane Gauges.
It sell, calibrate, service and repair industrial and commercial scales of all types. In particular, Truck scales, floor scales, counting scales and benchtop scales.
There is no website for Harbor Lane Gauges, but we have three affiliates that have their own websites:
https://www.tallyloadworks.com/
https://northbendbalanceandmeasure.com/
https://kvbalance.com/
Target Market(s)
Industrial and Commercial Weighing systems
Industry/Entity Type
Look and feel
Each slider illustrates characteristics of the customer's brand and the style your logo design should communicate.

```html
<!DOCTYPE html>
<html lang="en">
<head>
<meta charset="utf-8">
<title>Harbor Lane Gauges – Board Presentation Template</title>
<link href="https://fonts.googleapis.com/css2?family=Arimo:wght@400;700&display=swap" rel="stylesheet">
<style>
  :root {
    --backdrop-light: #5a5a5a;
    --backdrop-dark: #2f2f2f;
    --slide-bg: #ffffff;
    --brand-red: #d13a30;
    --brand-charcoal: #2c3942;
    --brand-grey: #47525a;
    --brand-blue: #2f5f8f;
    --body-ink: #111111;
    --frame: #000000;
  }
  * { margin: 0; padding: 0; box-sizing: border-box; }
  html, body { width: 1200px; height: 960px; overflow: hidden; }
  body {
    background: radial-gradient(ellipse at 50% 45%, var(--backdrop-light) 0%, var(--backdrop-dark) 100%);
    font-family: "Arimo", Arial, sans-serif;
    position: relative;
  }
  .slide {
    position: absolute;
    width: 668px;
    height: 502px;
    background: var(--slide-bg);
    overflow: hidden;
    transform: scale(0.8);
    transform-origin: 0 0;
  }
  .slide--cover { left: 51px; top: 62px; }
  .slide--two-column { left: 612px; top: 62px; }
  .slide--gallery { left: 44px; top: 496px; }
  .slide--closing { left: 621px; top: 496px; }

  .bands { position: absolute; inset: 0; width: 668px; height: 502px; }

  .wordmark {
    position: absolute;
    display: flex;
    align-items: center;
    color: var(--brand-grey);
    font-weight: 700;
    text-transform: uppercase;
    line-height: 1.05;
  }
  .wordmark__dot { border-radius: 50%; background: var(--brand-red); flex: none; }
  .wordmark--large { left: 140px; top: 62px; font-size: 40px; letter-spacing: 1px; gap: 22px; }
  .wordmark--large .wordmark__dot { width: 58px; height: 58px; }
  .wordmark--centered {
    left: 0; right: 0; top: 190px; flex-direction: column; gap: 22px;
    font-size: 40px; letter-spacing: 1px; text-align: center;
  }
  .wordmark--centered .wordmark__dot { width: 76px; height: 76px; }
  .wordmark--small {
    left: 528px; top: 20px; width: 112px; flex-direction: column; gap: 6px;
    font-size: 12px; text-align: center;
  }
  .wordmark--small .wordmark__dot { width: 24px; height: 24px; }

  .slide-title {
    position: absolute; top: 50px; color: #fff;
    font-size: 33px; font-weight: 700; letter-spacing: 0.5px;
  }
  .slide--two-column .slide-title { left: 48px; }
  .slide--gallery .slide-title { left: 50px; }

  .body-copy {
    position: absolute; color: var(--body-ink);
    font-size: 12.4px; line-height: 15.6px; text-align: justify;
  }
  .body-copy--left { left: 47px; top: 178px; width: 258px; }
  .body-copy--right { left: 353px; top: 178px; width: 258px; }
  .body-copy--wide { left: 51px; top: 145px; width: 561px; }

  .hero-photo {
    position: absolute; left: 0; top: 268px; width: 668px; height: 177px;
    background: linear-gradient(100deg, #d9dadb 0%, #c9cbcd 40%, #e6b23a 70%, #e9eaeb 100%);
  }
  .thumb {
    position: absolute; top: 337px; width: 175px; height: 123px;
    border: 5px solid var(--frame);
  }
  .thumb--one { left: 52px; background: linear-gradient(160deg, #9aa3ad, #b5734a); }
  .thumb--two { left: 244px; background: linear-gradient(160deg, #5a6470, #c9a64a); }
  .thumb--three { left: 435px; background: linear-gradient(160deg, #c79a6a, #8d3a34); }
</style>
</head>
<body>

  <section class="slide slide--cover">
    <div class="wordmark wordmark--large">
      <span class="wordmark__dot"></span>
      <span>Harbor Lane<br>Gauges</span>
    </div>
    <svg class="bands" viewBox="0 0 668 502" aria-hidden="true">
      <polygon fill="var(--brand-red)" points="0,190 285,190 307,212 668,212 668,218 0,218"/>
      <rect fill="var(--brand-charcoal)" x="0" y="218" width="668" height="50"/>
      <rect fill="var(--brand-charcoal)" x="0" y="445" width="668" height="15"/>
      <polygon fill="var(--brand-charcoal)" points="336,460 668,460 668,502 372,502"/>
    </svg>
    <div class="hero-photo" role="img" aria-label="Yellow semi truck with white trailer parked on a blue truck scale at a loading dock"></div>
  </section>

  <section class="slide slide--two-column">
    <svg class="bands" viewBox="0 0 668 502" aria-hidden="true">
      <polygon fill="var(--brand-red)" points="0,14 283,14 303,35 528,35 528,44 0,44"/>
      <rect fill="var(--brand-red)" x="640" y="37" width="28" height="7"/>
      <rect fill="var(--brand-charcoal)" x="0" y="44" width="528" height="50"/>
      <rect fill="var(--brand-charcoal)" x="640" y="44" width="28" height="50"/>
    </svg>
    <h1 class="slide-title">TITLE HERE</h1>
    <div class="wordmark wordmark--small">
      <span class="wordmark__dot"></span>
      <span>Harbor Lane Gauges</span>
    </div>
    <p class="body-copy body-copy--left">Lorem Ipsum is simply dummy text of the printing and typesetting industry. Lorem Ipsum has been the industry's standard dummy text ever since the 1500s, when an unknown printer took a galley of type and scrambled it to make a type specimen book. It has survived not only five centuries, but also the leap into electronic typesetting, remaining essentially unchanged. It was popularised in the 1960s with the release of Presstype sheets containing Lorem Ipsum passages, and more recently with desktop publishing software like Quillset Layout including versions of Lorem Ipsum.</p>
    <p class="body-copy body-copy--right">Lorem Ipsum is simply dummy text of the printing and typesetting industry. Lorem Ipsum has been the industry's standard dummy text ever since the 1500s, when an unknown printer took a galley of type and scrambled it to make a type specimen book. It has survived not only five centuries, but also the leap into electronic typesetting, remaining essentially unchanged. It was popularised in the 1960s with the release of Presstype sheets containing Lorem Ipsum passages, and more recently with desktop publishing software like Quillset Layout including versions of Lorem Ipsum.</p>
  </section>

  <section class="slide slide--gallery">
    <svg class="bands" viewBox="0 0 668 502" aria-hidden="true">
      <polygon fill="var(--brand-red)" points="0,16 283,16 303,37 528,37 528,46 0,46"/>
      <rect fill="var(--brand-red)" x="640" y="39" width="28" height="7"/>
      <rect fill="var(--brand-charcoal)" x="0" y="46" width="528" height="50"/>
      <rect fill="var(--brand-charcoal)" x="640" y="46" width="28" height="50"/>
    </svg>
    <h1 class="slide-title">TITLE HERE</h1>
    <div class="wordmark wordmark--small" style="top:22px">
      <span class="wordmark__dot"></span>
      <span>Harbor Lane Gauges</span>
    </div>
    <p class="body-copy body-copy--wide">Lorem Ipsum is simply dummy text of the printing and typesetting industry. Lorem Ipsum has been the industry's standard dummy text ever since the 1500s, when an unknown printer took a galley of type and scrambled it to make a type specimen book. It has survived not only five centuries, but also the leap into electronic typesetting, remaining essentially unchanged. It was popularised in the 1960s with the release of Presstype sheets containing Lorem Ipsum passages, and more recently with desktop publishing software like Quillset Layout including versions of Lorem Ipsum.</p>
    <div class="thumb thumb--one" role="img" aria-label="Red truck driving onto an orange truck scale on a city street"></div>
    <div class="thumb thumb--two" role="img" aria-label="Truck wheels resting on a yellow weighbridge with a digital indicator"></div>
    <div class="thumb thumb--three" role="img" aria-label="Dump truck standing on a red weighbridge"></div>
  </section>

  <section class="slide slide--closing">
    <svg class="bands" viewBox="0 0 668 502" aria-hidden="true">
      <polygon fill="var(--brand-red)" points="0,57 288,57 308,78 668,78 668,85 0,85"/>
      <rect fill="var(--brand-charcoal)" x="0" y="85" width="668" height="50"/>
      <rect fill="var(--brand-charcoal)" x="0" y="392" width="668" height="50"/>
      <polygon fill="var(--brand-red)" points="0,442 668,442 668,470 390,470 368,449 0,449"/>
    </svg>
    <div class="wordmark wordmark--centered">
      <span class="wordmark__dot"></span>
      <span>Harbor Lane<br>Gauges</span>
    </div>
  </section>

</body>
</html>
```